Larkspur Ridge Management - Business Cards

I need business cards. My current logo was designed by a designer at this site and I very much like and am happy with the results. I would like a business card that is trendy, unique, current yet professional. I deal with high net worth clients daily

Target Market(s)

Out of state investors looking to get into the rental market in Ohio

Industry/Entity Type

Property Management, Consulting

Contact Information for Business Card

Name, Title (Chief Financial Officer) office phone number (555) 817-3094 website address larkridgemgmt.example

Font styles to use
Sans Serif

Colors
0054AA
0677BA
7BADD7
CADEEF
E8F1F8
0094D4
00A9DD
6FCCEA
C7EBF8
E9F6FB
00AB8E
00BBA5
67D7C9
C6EFE9
E9F9F6

```html
<!DOCTYPE html>
<html lang="en">
<head>
<meta charset="utf-8">
<title>Larkspur Ridge Management – Business Card</title>
<link rel="stylesheet" href="https://fonts.googleapis.com/css2?family=Montserrat:wght@500;600;700&display=swap">
<style>
  :root {
    --navy: #22375a;
    --red: #d12a2a;
    --paper: #ffffff;
    --pattern-light: #f7f7f9;
    --pattern-mid: #e9e9ef;
    --page: #ffffff;
    --shadow: rgba(20, 30, 50, 0.28);
  }
  * { box-sizing: border-box; margin: 0; padding: 0; }
  html, body {
    width: 998px;
    height: 1200px;
    overflow: hidden;
    background: var(--page);
    font-family: "Montserrat", sans-serif;
  }
  .stage {
    position: relative;
    width: 998px;
    height: 1200px;
  }
  .card {
    position: absolute;
    left: 149px;
    top: 400px;
    width: 700px;
    height: 400px;
    background: var(--paper);
    box-shadow: 0 14px 22px -6px var(--shadow);
    overflow: hidden;
  }
  .card__texture {
    position: absolute;
    inset: 0 0 50px 0;
    background: linear-gradient(100deg, var(--paper) 0%, var(--paper) 30%, var(--pattern-light) 55%, var(--pattern-mid) 100%);
  }
  .card__person {
    position: absolute;
    left: 45px;
    top: 44px;
  }
  .card__name {
    font-size: 49px;
    font-weight: 700;
    color: var(--navy);
    letter-spacing: 0.2px;
    line-height: 1;
  }
  .card__title {
    margin-top: 10px;
    font-size: 20.5px;
    font-weight: 500;
    color: var(--red);
    line-height: 1;
  }
  .contact {
    position: absolute;
    left: 48px;
    top: 176px;
    list-style: none;
  }
  .contact__item {
    display: flex;
    align-items: center;
    height: 32px;
    margin-bottom: 20px;
    font-size: 19px;
    font-weight: 500;
    color: var(--navy);
  }
  .contact__item:nth-child(2) { margin-bottom: 23px; }
  .contact__icon {
    width: 32px;
    height: 32px;
    margin-right: 12px;
    flex: none;
  }
  .brand {
    position: absolute;
    left: 440px;
    top: 130px;
    width: 220px;
    display: flex;
    align-items: center;
    gap: 12px;
  }
  .brand__dot {
    width: 26px;
    height: 26px;
    border-radius: 50%;
    background: var(--navy);
    flex: none;
  }
  .brand__name {
    font-size: 22px;
    font-weight: 700;
    color: var(--navy);
    line-height: 1.2;
  }
  .card__band {
    position: absolute;
    left: 0;
    bottom: 0;
    width: 100%;
    height: 50px;
    background: var(--navy);
    display: flex;
    align-items: center;
    justify-content: center;
    color: #ffffff;
    font-size: 18px;
    font-weight: 500;
    letter-spacing: 0.2px;
  }
</style>
</head>
<body>
<main class="stage">
  <section class="card">
    <div class="card__texture" role="img" aria-label="Faint repeating pattern of light grey shapes across the card background"></div>

    <header class="card__person">
      <h1 class="card__name">Dana Whitfield</h1>
      <p class="card__title">CHIEF FINANCIAL OFFICER</p>
    </header>

    <ul class="contact">
      <li class="contact__item">
        <svg class="contact__icon" viewBox="0 0 32 32" aria-hidden="true">
          <rect x="4" y="4" width="20" height="24" rx="2" fill="none" stroke="var(--red)" stroke-width="2.2"/>
          <rect x="24" y="6" width="4" height="20" rx="1" fill="none" stroke="var(--red)" stroke-width="2.2"/>
          <rect x="8" y="8" width="12" height="5" fill="none" stroke="var(--red)" stroke-width="1.8"/>
          <g fill="var(--red)">
            <rect x="8" y="16" width="3" height="3"/><rect x="12.5" y="16" width="3" height="3"/><rect x="17" y="16" width="3" height="3"/>
            <rect x="8" y="21" width="3" height="3"/><rect x="12.5" y="21" width="3" height="3"/><rect x="17" y="21" width="3" height="3"/>
          </g>
        </svg>
        (555) 817-3094
      </li>
      <li class="contact__item">
        <svg class="contact__icon" viewBox="0 0 32 32" aria-hidden="true">
          <g fill="none" stroke="var(--red)" stroke-width="2">
            <circle cx="16" cy="16" r="13"/>
            <ellipse cx="16" cy="16" rx="6" ry="13"/>
            <line x1="3" y1="16" x2="29" y2="16"/>
            <path d="M5.5 9.5h21M5.5 22.5h21"/>
          </g>
        </svg>
        www.larkridgemgmt.example
      </li>
      <li class="contact__item">
        <svg class="contact__icon" viewBox="0 0 32 32" aria-hidden="true">
          <circle cx="16" cy="16" r="15" fill="var(--red)"/>
          <path d="M16 8.5a5 5 0 0 0-5 5c0 3.6 5 9 5 9s5-5.4 5-9a5 5 0 0 0-5-5z" fill="#fff"/>
          <circle cx="16" cy="13.5" r="1.8" fill="var(--red)"/>
        </svg>
        Fairbrook, Ohio 43099
      </li>
    </ul>

    <div class="brand">
      <span class="brand__dot"></span>
      <span class="brand__name">Larkspur Ridge Management</span>
    </div>

    <footer class="card__band">PROFESSIONAL MANAGEMENT. TRUSTED RESULTS.</footer>
  </section>
</main>
</body>
</html>
```